International Hand & Body company needing a Hand cream tube design for the Retail market

I am wanting a modern design for a new range of 6 hand creams I will be launching in August. They need to compliment our range of wrapped soaps which you can see on www.plomvane.com.au so am wanting clean designs. I am wanting a solid colour with a hand drawn organic feel line drawing in black elegantly placed wrapping around the label. I am wanting to focus on the colour and positioning of words and fonts. I like modern clean contemporary fonts. The final design needs to appeal to the broader female market.This may lead to range expansion if designs are well received.
Updates

These designs are not hitting the brief. They are too generic and look like a supermarket brand. Our brand is more boutique and this design needs to be modern and simple. I would like more solid colours and more modern designs. Without patterns.

Target Market(s)

Female aged 20 - 70

Requirements
Must have
• a modern contemporary design that will appeal to the masses.
• Please read attached brief.
Should not have
• a black botanical illustration, in a loose and organic design to match the fragrance.

```html
<!DOCTYPE html>
<html lang="en">
<head>
<meta charset="utf-8">
<title>Plomvane Hand Cream – Label Range</title>
<link href="https://fonts.googleapis.com/css2?family=Parisienne&family=Quicksand:wght@400;600&display=swap" rel="stylesheet">
<style>
  :root {
    --canvas: #ffffff;
    --grey: #717170;
    --yellow: #fbb809;
    --coral: #ec6f58;
    --teal: #2d717f;
    --pink: #e85b73;
    --peach: #e8c4aa;
    --plum: #59445e;
    --ink: #262626;
    --white: #ffffff;
    --lemon-light: #f6db78;
    --lemon-deep: #ffc600;
    --coral-light: #ee6d57;
    --coral-deep: #e8543e;
    --gold-light: #b9843a;
    --gold-deep: #7f5a2d;
    --script: "Parisienne", cursive;
    --sans: "Quicksand", sans-serif;
  }
  html, body { margin: 0; padding: 0; overflow: hidden; }
  body { width: 1200px; height: 1200px; background: var(--canvas); position: relative; font-family: var(--sans); }

  .label { position: absolute; width: 111px; height: 305px; overflow: hidden; background: var(--bg); color: var(--fg); }
  .col-1 { left: 78px; } .col-2 { left: 268px; } .col-3 { left: 458px; }
  .row-1 { top: 78px; } .row-2 { top: 462px; } .row-3 { top: 846px; }

  .label__top { position: absolute; left: 0; top: 0; width: 100%; height: 153px; background: var(--top); }
  .label__bottom { position: absolute; left: 0; top: 153px; width: 100%; height: 152px; background: var(--bottom); }

  .line { position: absolute; left: 0; right: 0; margin: 0; text-align: center; white-space: nowrap; transform: translateY(-50%); }

  .scent { font-family: var(--script); font-size: 21px; line-height: 1; color: var(--scent-colour, var(--white)); }
  .brand { font-weight: 600; font-size: 11px; letter-spacing: 1.6px; color: var(--brand-colour, var(--fg)); }
  .product { font-size: 9.5px; letter-spacing: 0.2px; }
  .claim { font-size: 9.5px; line-height: 12px; transform: none; }
  .volume { font-size: 14.5px; }
  .origin { font-size: 9.5px; }

  .band { position: absolute; left: 0; top: 0; width: 111px; height: 305px; }

  .yuzu-split { --top: var(--grey); --bottom: var(--yellow); --fg: var(--ink); }
  .citrus-split { --top: var(--coral); --bottom: var(--teal); --fg: #1f2b2e; }
  .fig-split { --top: var(--pink); --bottom: var(--peach); --fg: var(--ink); }

  .yuzu-solid { --bg: var(--grey); --fg: var(--white); }
  .citrus-solid { --bg: var(--teal); --fg: var(--white); }
  .fig-solid { --bg: var(--plum); --fg: var(--white); }

  .yuzu-ribbon { --bg: var(--grey); --fg: var(--lemon-light); --scent-colour: var(--lemon-light); }
  .citrus-ribbon { --bg: var(--teal); --fg: var(--coral); --scent-colour: var(--coral); }
  .fig-ribbon { --bg: var(--plum); --fg: var(--gold-light); --scent-colour: var(--gold-light); }
</style>
</head>
<body>

<!-- Row one: split colour labels -->
<section class="label yuzu-split col-1 row-1">
  <div class="label__top"></div><div class="label__bottom"></div>
  <p class="line scent" style="top:47px">Yuzu</p>
  <p class="line scent" style="top:74px">and</p>
  <p class="line scent" style="top:101px">Sage</p>
  <p class="line brand" style="top:171px">plomvane</p>
  <p class="line product" style="top:188px">HAND CREAM</p>
  <p class="line claim" style="top:204px">“A nourishing<br>non-greasy hand<br>cream to keep skin<br>soft and hydrated”</p>
  <p class="line volume" style="top:277px">35ml</p>
  <p class="line origin" style="top:293px">made in Australia</p>
</section>

<section class="label citrus-split col-2 row-1">
  <div class="label__top"></div><div class="label__bottom"></div>
  <p class="line scent" style="top:49px">Citrus</p>
  <p class="line scent" style="top:76px">and</p>
  <p class="line scent" style="top:103px">Seagrass</p>
  <p class="line brand" style="top:171px">plomvane</p>
  <p class="line product" style="top:188px">HAND CREAM</p>
  <p class="line claim" style="top:204px">“A nourishing<br>non-greasy hand<br>cream to keep skin<br>soft and hydrated”</p>
  <p class="line volume" style="top:277px">35ml</p>
  <p class="line origin" style="top:293px">made in Australia</p>
</section>

<section class="label fig-split col-3 row-1">
  <div class="label__top"></div><div class="label__bottom"></div>
  <p class="line scent" style="top:56px">Fig</p>
  <p class="line scent" style="top:83px">and</p>
  <p class="line scent" style="top:110px">Sandalwood</p>
  <p class="line brand" style="top:171px">plomvane</p>
  <p class="line product" style="top:188px">HAND CREAM</p>
  <p class="line claim" style="top:204px">“A nourishing<br>non-greasy hand<br>cream to keep skin<br>soft and hydrated”</p>
  <p class="line volume" style="top:277px">35ml</p>
  <p class="line origin" style="top:293px">made in Australia</p>
</section>

<!-- Row two: solid colour labels -->
<section class="label yuzu-solid col-1 row-2">
  <p class="line scent" style="top:45px">Yuzu</p>
  <p class="line scent" style="top:64px">and</p>
  <p class="line scent" style="top:83px">Sage</p>
  <p class="line brand" style="top:153px">plomvane</p>
  <p class="line product" style="top:188px">HAND CREAM</p>
  <p class="line claim" style="top:204px">“A nourishing<br>non-greasy hand<br>cream to keep skin<br>soft and hydrated”</p>
  <p class="line volume" style="top:277px">35ml</p>
  <p class="line origin" style="top:293px">made in Australia</p>
</section>

<section class="label citrus-solid col-2 row-2">
  <p class="line scent" style="top:47px">Citrus</p>
  <p class="line scent" style="top:66px">and</p>
  <p class="line scent" style="top:85px">Seagrass</p>
  <p class="line brand" style="top:153px">plomvane</p>
  <p class="line product" style="top:188px">HAND CREAM</p>
  <p class="line claim" style="top:204px">“A nourishing<br>non-greasy hand<br>cream to keep skin<br>soft and hydrated”</p>
  <p class="line volume" style="top:277px">35ml</p>
  <p class="line origin" style="top:293px">made in Australia</p>
</section>

<section class="label fig-solid col-3 row-2">
  <p class="line scent" style="top:55px">Fig</p>
  <p class="line scent" style="top:72px">and</p>
  <p class="line scent" style="top:91px">Sandalwood</p>
  <p class="line brand" style="top:153px">plomvane</p>
  <p class="line product" style="top:188px">HAND CREAM</p>
  <p class="line claim" style="top:204px">“A nourishing<br>non-greasy hand<br>cream to keep skin<br>soft and hydrated”</p>
  <p class="line volume" style="top:277px">35ml</p>
  <p class="line origin" style="top:293px">made in Australia</p>
</section>

<!-- Row three: crossed ribbon labels -->
<section class="label yuzu-ribbon col-1 row-3">
  <svg class="band" viewBox="0 0 111 305" aria-hidden="true">
    <polygon points="0,104 111,79 111,104 0,129" fill="var(--lemon-deep)"/>
    <polygon points="0,79 111,104 111,129 0,104" fill="var(--lemon-light)"/>
  </svg>
  <p class="line scent" style="top:28px">Yuzu</p>
  <p class="line scent" style="top:47px">and</p>
  <p class="line scent" style="top:66px">Sage</p>
  <p class="line brand" style="top:153px">plomvane</p>
  <p class="line product" style="top:188px">HAND CREAM</p>
  <p class="line claim" style="top:204px">“A nourishing<br>non-greasy hand<br>cream to keep skin<br>soft and hydrated”</p>
  <p class="line volume" style="top:277px">35ml</p>
  <p class="line origin" style="top:293px">made in Australia</p>
</section>

<section class="label citrus-ribbon col-2 row-3">
  <svg class="band" viewBox="0 0 111 305" aria-hidden="true">
    <polygon points="0,100 111,75 111,100 0,125" fill="var(--coral-deep)"/>
    <polygon points="0,75 111,100 111,125 0,100" fill="var(--coral-light)"/>
  </svg>
  <p class="line scent" style="top:28px">Citrus</p>
  <p class="line scent" style="top:47px">and</p>
  <p class="line scent" style="top:66px">Seagrass</p>
  <p class="line brand" style="top:153px">plomvane</p>
  <p class="line product" style="top:188px">HAND CREAM</p>
  <p class="line claim" style="top:204px">“A nourishing<br>non-greasy hand<br>cream to keep skin<br>soft and hydrated”</p>
  <p class="line volume" style="top:277px">35ml</p>
  <p class="line origin" style="top:293px">made in Australia</p>
</section>

<section class="label fig-ribbon col-3 row-3">
  <svg class="band" viewBox="0 0 111 305" aria-hidden="true">
    <polygon points="0,100 111,75 111,100 0,125" fill="var(--gold-deep)"/>
    <polygon points="0,75 111,100 111,125 0,100" fill="var(--gold-light)"/>
  </svg>
  <p class="line scent" style="top:19px">Fig</p>
  <p class="line scent" style="top:36px">and</p>
  <p class="line scent" style="top:55px">Sandalwood</p>
  <p class="line brand" style="top:153px">plomvane</p>
  <p class="line product" style="top:188px">HAND CREAM</p>
  <p class="line claim" style="top:204px">“A nourishing<br>non-greasy hand<br>cream to keep skin<br>soft and hydrated”</p>
  <p class="line volume" style="top:277px">35ml</p>
  <p class="line origin" style="top:293px">made in Australia</p>
</section>

</body>
</html>
```